Emergency Management Consulting Needs a Website

Need to develop a website for an Emergency Management Consulting business. This website needs to be user friendly and resemble disaster preparedness, response, recovery, and mitigation. It must allow for me to make changes to it myself by adding pages, content and pictures. Looking for an advanced page to the website that allows monitoring of social media sites, hashtags, and keywords. Must have pictures of disasters on the site. Must try to integrate the logo colors, not excessive.

Reason: Did not receive anything sufficient to what I am looking for.

Industry/Entity Type

Government

Coding

Coded - Design and coding required

Number of Pages Required

5+ page

Requirements
Must have
• Logo, advanced social media monitoring page, allow for edits myself (content, pages, graphics) this must be a CMS of some sort, use logo color scheme (not excessively), must be professional looking, connect with Pexaro Domain, find a hosting site, SEO, no "long" designs, minimize "dead" space, no social media feeds, no newsletter stuff.
• Menu items: Home, About Us, Services, Situation Monitor, Work With Us, Contact Us (hopefully these could be editable if I need to later)
• When you make a submission, please send me a message on which CMS you are using. Thank you.
Nice to have
• Examples of websites:
• https://www.qarl.vic.gov.au/
• http://www.malvecorish.com/
• http://www.tuvrakol.org/
• http://pomvaleconsulting.com/
• http://www.sultavon.com/services/emergency-management
• https://uzo.com/
• http://www.velumbra.com/Responsibility/Sustainable-Development/HSE/Crisis-and-Emergency-Management/

```html
<!DOCTYPE html>
<html lang="en">
<head>
<meta charset="utf-8">
<title>Calder Fork Emergency Management</title>
<link href="https://fonts.googleapis.com/css2?family=Montserrat:wght@700&family=Open+Sans:wght@400;600;700&family=Teko:wght@400;500&display=swap" rel="stylesheet">
<style>
:root{
  --white:#ffffff;
  --ink:#333333;
  --muted:#666666;
  --blue:#1565c0;
  --blue-card:#2e86d1;
  --blue-btn:#4f87c7;
  --accent-red:#e0483a;
  --orange:#e07a1c;
  --orange-btn:#d9701a;
  --footer:#2d2d2d;
  --footer-bar:#1e1e1e;
  --footer-text:#ffffff;
}
*{margin:0;padding:0;box-sizing:border-box}
html,body{width:1200px;height:2287px;overflow:hidden;background:var(--white)}
body{position:relative;font-family:"Open Sans",Arial,sans-serif;color:var(--ink)}
.abs{position:absolute}

/* header */
.site-header{left:0;top:0;width:1200px;height:96px;background:var(--white)}
.brand{left:100px;top:26px;display:flex;align-items:center;gap:12px}
.brand-dot{width:44px;height:44px;border-radius:50%;background:var(--blue)}
.brand-name{font-weight:700;font-size:27px;color:var(--ink);letter-spacing:1px}
.main-nav{left:506px;top:0;height:96px;display:flex}
.main-nav a{display:block;height:96px;line-height:124px;padding:0 14px;font-size:14px;color:#444;text-decoration:none;position:relative}
.main-nav a.is-active{color:var(--ink)}
.main-nav a.is-active::after{content:"";position:absolute;left:3px;right:3px;top:90px;height:3px;background:var(--accent-red)}

/* hero */
.hero{left:0;top:96px;width:1200px;height:521px;overflow:hidden;
  background:linear-gradient(180deg,#4a5360 0%,#3b4a5a 40%,#1f3550 75%,#16283f 100%)}
.hero-photo{position:absolute;inset:0;background:
  radial-gradient(ellipse at 90% 15%,rgba(20,20,20,.85) 0%,rgba(20,20,20,0) 35%),
  radial-gradient(ellipse at 40% 45%,rgba(200,200,200,.35) 0%,rgba(200,200,200,0) 40%)}
.hero-wedge{position:absolute;left:0;top:0}
.hero-title{left:545px;top:180px;width:620px;font-family:"Montserrat",Arial,sans-serif;font-weight:700;font-size:40px;line-height:46px;color:var(--white);letter-spacing:.5px}
.hero-text{left:546px;top:274px;font-size:14px;line-height:27px;color:var(--white);white-space:nowrap}
.btn-learn{left:553px;top:351px;width:187px;height:45px;background:var(--blue-btn);color:var(--white);font-size:14px;font-weight:600;text-align:center;line-height:45px}

/* services */
.section-title{left:0;top:668px;width:1200px;text-align:center;font-family:"Teko",Arial,sans-serif;font-size:64px;font-weight:400;line-height:76px;color:#222}
.title-rule{top:712px;height:1px;background:linear-gradient(90deg,rgba(0,0,0,0),#999)}
.title-rule.right{background:linear-gradient(90deg,#999,rgba(0,0,0,0))}
.section-sub{left:0;top:747px;width:1200px;text-align:center;font-size:13px;color:var(--muted)}
.service-card{width:258px;height:271px;overflow:hidden}
.service-card .photo{position:absolute;inset:0}
.service-card .label{position:absolute;left:0;right:0;bottom:0;height:72px;background:rgba(40,40,40,.8);color:var(--white);font-family:"Teko",Arial,sans-serif;font-weight:400;font-size:36px;line-height:80px;text-align:center}
.service-card.feature{background:var(--blue-card);color:var(--white);text-align:center;padding:52px 22px 0}
.feature h3{font-size:14px;font-weight:700;line-height:24px;margin-bottom:8px}
.feature p{font-size:13px;line-height:20px}

/* cta band */
.cta{left:0;top:1476px;width:1200px;height:437px;
  background:linear-gradient(180deg,#1e68c4 0%,#1a62bc 60%,#1759ad 100%)}
.cta-dot{left:570px;top:1520px;width:60px;height:60px;border-radius:50%;background:var(--orange)}
.cta-rule{left:410px;top:1640px;width:380px;height:1px;background:rgba(255,255,255,.5)}
.cta-title{left:0;top:1643px;width:1200px;text-align:center;font-family:"Teko",Arial,sans-serif;font-weight:400;font-size:36px;line-height:40px;color:var(--white)}
.cta-text{left:150px;top:1702px;width:900px;text-align:center;font-size:13px;line-height:23px;color:var(--white)}
.btn-more{left:472px;top:1787px;width:224px;height:46px;background:var(--orange-btn);color:var(--white);font-size:14px;display:flex;align-items:center;justify-content:center;gap:10px}

/* footer */
.site-footer{left:0;top:1913px;width:1200px;height:324px;background:var(--footer)}
.footer-heading{font-family:"Teko",Arial,sans-serif;font-weight:400;font-size:24px;color:var(--orange);line-height:30px}
.blog,.contact,.hello{color:var(--footer-text)}
.blog{left:108px;top:1946px;width:288px;font-size:13px;line-height:20px}
.blog .body{text-align:justify}
.blog .date{color:var(--orange);font-size:12px}
.blog .read{color:var(--orange);font-size:12px;margin-left:3px}
.contact{left:506px;top:1943px;width:300px;font-size:13px}
.contact-row{display:flex;align-items:flex-start;line-height:19px}
.contact-row svg{width:14px;height:14px;margin:2px 14px 0 0;flex:none}
.contact-row b{width:62px;flex:none;font-weight:700}
.hello{left:807px;top:1943px;width:234px;font-size:13px}
.hello label{display:block;font-weight:700;line-height:20px}
.field{width:232px;height:29px;background:var(--white);margin-top:2px}
.field.tall{height:46px}
.btn-submit{left:950px;top:2191px;width:90px;height:32px;background:#0f55a8;color:var(--white);font-family:Arial,sans-serif;font-size:13px;text-align:center;line-height:32px}
.copyright{left:0;top:2237px;width:1200px;height:50px;background:var(--footer-bar);color:#9a9a9a;font-family:Arial,sans-serif;font-size:13px;text-align:center;line-height:46px}
</style>
</head>
<body>

<header class="site-header abs">
  <div class="brand abs"><span class="brand-dot"></span><span class="brand-name">CALDER FORK</span></div>
  <nav class="main-nav abs">
    <a href="#" class="is-active">Home</a>
    <a href="#">About Us</a>
    <a href="#">Services</a>
    <a href="#">Situation Monitor</a>
    <a href="#">Work With Us</a>
    <a href="#">Contact Us</a>
  </nav>
</header>

<section class="hero abs">
  <div class="hero-photo" role="img" aria-label="Harbour scene with a cruise ship, tug boats and black smoke from a fire"></div>
  <svg class="hero-wedge" width="470" height="521" viewBox="0 0 470 521">
    <polygon points="0,0 0,140 140,360 0,430 0,521 460,521 225,270 450,0" fill="#1a5fc0" opacity=".55"/>
    <polygon points="0,0 0,140 140,360 0,430 0,521 300,521 70,270 290,0" fill="#1a5fc0" opacity=".35"/>
  </svg>
  <h1 class="hero-title abs">CALDER FORK EMERGENCY MANAGEMENT</h1>
  <p class="hero-text abs">We strive for a perfect delivery and promise to be there for anything you may need, every step of the way.<br>Click here to find out more about Freight Management and how we do it.</p>
  <div class="btn-learn abs">LEARN MORE</div>
</section>

<h2 class="section-title abs">Our Sevices</h2>
<div class="title-rule abs" style="left:310px;width:195px"></div>
<div class="title-rule right abs" style="left:725px;width:210px"></div>
<p class="section-sub abs">Lorem Ipsum is simply dummy text of the printing and typesetting industry.</p>

<div class="service-card feature abs" style="left:161px;top:824px">
  <h3>9/11 EXPEDITED PUBLIC ASSISTANCE CLOSEOUT</h3>
  <p>Pomvale was given six months to reengineer the NERA closeout process dealing with approximately $5 billion in public assistance grants and an additional $2.4 billion in 9/11 associated costs.</p>
</div>
<div class="service-card abs" style="left:469px;top:824px">
  <div class="photo" role="img" aria-label="Boat on fire with heavy black smoke over water" style="background:linear-gradient(180deg,#2a2a2a 0%,#555 45%,#c2502a 65%,#6a7480 100%)"></div>
  <div class="label">WILMINGTON, NC</div>
</div>
<div class="service-card abs" style="left:775px;top:824px">
  <div class="photo" role="img" aria-label="Cruise ship in a fjord between snowy mountains" style="background:linear-gradient(180deg,#7fb0e0 0%,#6a7a80 35%,#3d5a7a 60%,#1d4e8a 100%)"></div>
  <div class="label">WILMINGTON, NC</div>
</div>
<div class="service-card abs" style="left:161px;top:1137px">
  <div class="photo" role="img" aria-label="City street lined with colourful buildings" style="background:linear-gradient(180deg,#c9d3dd 0%,#a89888 40%,#7a6a5c 70%,#5a5858 100%)"></div>
  <div class="label">New York, NC</div>
</div>
<div class="service-card abs" style="left:469px;top:1137px">
  <div class="photo" role="img" aria-label="Suspension bridge at dusk with city lights" style="background:linear-gradient(180deg,#3c7080 0%,#2a4050 45%,#8a6a30 70%,#c89840 100%)"></div>
  <div class="label">New York, NC</div>
</div>
<div class="service-card abs" style="left:775px;top:1137px">
  <div class="photo" role="img" aria-label="Busy city square with bright signs and a yellow taxi" style="background:linear-gradient(180deg,#5a3040 0%,#a03a3a 40%,#d0a030 75%,#555 100%)"></div>
  <div class="label">New York, NC</div>
</div>

<section class="cta abs" role="img" aria-label="Blue-tinted harbour scene with ships and smoke"></section>
<div class="cta-dot abs"></div>
<div class="cta-rule abs"></div>
<h2 class="cta-title abs">Calder Fork Emergency Management</h2>
<p class="cta-text abs">simply dummy text of the printing and typesetting industry. Lorem Ipsum has been the industry's standard dummy text ever since the 1500s,<br>when an unknown printer took a galley of type and scrambled it to make a type specimen book.</p>
<div class="btn-more abs">
  <svg width="14" height="14" viewBox="0 0 16 16" fill="none" stroke="#fff" stroke-width="1.8"><circle cx="8" cy="3" r="1.6"/><path d="M8 4.6V15M4.5 7h7M2 10c1 3 3.5 5 6 5s5-2 6-5"/></svg>
  MORE DETAILS
</div>

<footer class="site-footer abs"></footer>
<div class="blog abs">
  <h3 class="footer-heading">Calder Fork Blog</h3>
  <p style="margin-top:9px">Posted by: Calder Fork</p>
  <p>http://www.newsvantage.com/id/47278454/</p>
  <p class="date" style="margin-top:5px">5/4/2012</p>
  <p class="body">And once workforce balance has been achieved, ignite its capacity with transformational team-building programs!</p>
  <p class="read" style="margin-top:4px">Read More...</p>
</div>
<div class="contact abs">
  <h3 class="footer-heading">Contact Us</h3>
  <div class="contact-row" style="margin-top:17px">
    <svg viewBox="0 0 16 16"><path d="M8 1a5 5 0 0 0-5 5c0 4 5 9 5 9s5-5 5-9a5 5 0 0 0-5-5zm0 7a2 2 0 1 1 0-4 2 2 0 0 1 0 4z" fill="#fff"/></svg>
    <b>Address*</b><span>2400 Larkmere Ave<br>Easton Bay, CA 90000<br>United States</span>
  </div>
  <div class="contact-row" style="margin-top:9px">
    <svg viewBox="0 0 16 16"><path d="M3 1l3 3-1.5 2a9 9 0 0 0 5.5 5.5L12 10l3 3-2 2C7 15 1 9 1 3z" fill="#fff"/></svg>
    <b>Phone:</b><span>+48 555 010 234</span>
  </div>
  <div class="contact-row" style="margin-top:11px">
    <svg viewBox="0 0 16 16"><rect x="1" y="3" width="14" height="10" fill="#fff"/><path d="M1 3l7 6 7-6" stroke="#2d2d2d" stroke-width="1.4" fill="none"/></svg>
    <b>E-mail:</b><span>info@calderfork.com</span>
  </div>
  <div class="contact-row" style="margin-top:13px">
    <svg viewBox="0 0 16 16"><path d="M2 3h12v8H7l-4 3v-3H2z" fill="#fff"/></svg>
    <b>Chat:</b><span>calderfork</span>
  </div>
</div>
<div class="hello abs">
  <h3 class="footer-heading">Say Hello!</h3>
  <label style="margin-top:18px">Name*</label><div class="field"></div>
  <label style="margin-top:8px">Email*</label><div class="field"></div>
  <label style="margin-top:7px">Message*</label><div class="field tall"></div>
</div>
<div class="btn-submit abs">SUBMIT</div>
<div class="copyright abs">© Copyright 2016 Calder Fork Emergency Management. All Right Reserved.</div>

</body>
</html>
```